Business Card for IT company

I need a high tech looking business card using our logo. I prefer something clean and modern.

Target Market(s)

Buyers of IT hardware and software, IT Techies who are key influencers

Industry/Entity Type

Business

```html
<!DOCTYPE html>
<html lang="en">
<head>
<meta charset="utf-8">
<title>Corvane Consulting – Business Card</title>
<link rel="stylesheet" href="https://fonts.googleapis.com/css2?family=Exo+2:wght@300;600&display=swap">
<style>
  :root {
    --backdrop: #3b3b3b;
    --card-white: #f4f4f4;
    --card-white-edge: #d9d9d9;
    --brand-green: #6aa744;
    --brand-green-light: #8cc057;
    --brand-green-dark: #4f8c33;
    --ink-dark: #3a3a3a;
    --ink-light: #ffffff;
    --band-white: #ffffff;
  }
  * { margin: 0; padding: 0; box-sizing: border-box; }
  html, body {
    width: 1200px;
    height: 600px;
    overflow: hidden;
  }
  body {
    background: var(--backdrop);
    font-family: "Exo 2", "Segoe UI", sans-serif;
  }
  .canvas {
    position: relative;
    width: 1200px;
    height: 600px;
    display: flex;
    align-items: center;
    justify-content: center;
    gap: 60px;
  }
  .card {
    position: relative;
    width: 500px;
    height: 286px;
    overflow: hidden;
    box-shadow: 0 10px 28px rgba(0, 0, 0, 0.45);
  }

  /* Front: white face with company name */
  .card-front {
    background: radial-gradient(ellipse at 45% 45%, var(--card-white) 40%, var(--card-white-edge) 100%);
    display: flex;
    align-items: center;
    justify-content: center;
  }
  .company-name {
    font-weight: 600;
    font-size: 40px;
    letter-spacing: 1px;
    color: var(--ink-dark);
  }

  /* Back: green face with band and contact details */
  .card-back {
    background: radial-gradient(ellipse at 62% 42%, var(--brand-green-light) 0%, var(--brand-green) 55%, var(--brand-green-dark) 100%);
  }
  .accent-band {
    position: absolute;
    left: 0;
    top: 34%;
    width: 32%;
    height: 21%;
  }
  .contact {
    position: absolute;
    left: 33%;
    top: 37%;
    color: var(--ink-light);
    font-weight: 300;
    font-size: 17px;
    line-height: 26px;
    letter-spacing: 1.2px;
  }
  .contact-web { padding-left: 13px; }
</style>
</head>
<body>
  <main class="canvas">
    <section class="card card-front">
      <h1 class="company-name">Corvane Consulting</h1>
    </section>

    <section class="card card-back">
      <svg class="accent-band" viewBox="0 0 160 60" preserveAspectRatio="none" aria-hidden="true">
        <polygon points="0,0 160,0 130,60 0,60" fill="var(--band-white)"/>
      </svg>
      <div class="contact">
        <p class="contact-web">WWW.CORVANE.COM</p>
        <p class="contact-phone">555.013.0247</p>
      </div>
    </section>
  </main>
</body>
</html>
```